Rebranding our business - Business Cards

We are currently rebranding our business and have just completed our new logo and now are wanting to have new business cards designed.

I will upload our old business card design as we would like to keep the same information on the card, Including the icon dot points on the back. I will also upload other designs I would like placed on the cards.. Such as a character,

I would like our power statement to be:
KTW Removals -The Gentle Movers.

Instead of: Allow KTW Removals To Carry the Weight Of Every Relocation,

I am happy for the designer to run with their own ideas.

```html
<!DOCTYPE html>
<html lang="en">
<head>
<meta charset="utf-8">
<title>KTW Removals – Business Card</title>
<link rel="stylesheet" href="https://fonts.googleapis.com/css2?family=Open+Sans:wght@400;600;700&display=swap">
<style>
  :root {
    --stage: #000000;
    --card: #ffffff;
    --navy: #14246b;
    --ink: #1a1a1a;
    --brand-blue: #1f6fc1;
    --hero-orange: #f08a3c;
    --hero-navy: #2a3550;
  }
  * { margin: 0; padding: 0; box-sizing: border-box; }
  html, body {
    width: 1200px; height: 900px; overflow: hidden;
    background: var(--stage);
    font-family: "Open Sans", Arial, sans-serif;
  }
  .stage { position: relative; width: 1200px; height: 900px; }

  .card {
    position: absolute; top: 275px; width: 477px; height: 293px;
    background: var(--card); overflow: hidden;
  }
  .card--front { left: 116px; border-radius: 0 52px 0 52px; }
  .card--back  { left: 622px; border-radius: 52px 0 52px 0; }

  /* Front */
  .mascot {
    position: absolute; left: 4px; top: 6px; width: 150px; height: 238px;
    border-radius: 18px;
    background: linear-gradient(180deg, #f5f5f5 0%, #f6b27a 35%, var(--hero-orange) 55%, var(--hero-navy) 100%);
    opacity: .55;
  }
  .identity { position: absolute; right: 26px; top: 36px; text-align: right; color: var(--navy); }
  .identity__name { font-size: 18px; font-weight: 600; line-height: 1.2; }
  .identity__role { font-size: 12.5px; color: var(--ink); margin-top: 1px; }
  .address {
    position: absolute; right: 32px; top: 90px;
    font-size: 13px; color: var(--ink);
  }
  .contacts { position: absolute; right: 30px; top: 133px; list-style: none; }
  .contacts li {
    display: flex; justify-content: flex-end; align-items: center;
    font-size: 13px; color: var(--ink); height: 19.8px;
  }
  .contacts svg { width: 10px; height: 10px; margin-left: 6px; fill: var(--navy); }
  .power-band {
    position: absolute; left: 0; bottom: 0; width: 100%; height: 49px;
    background: var(--navy); color: #fff;
    font-size: 14px; font-weight: 600;
    display: flex; align-items: center; justify-content: center;
    padding-right: 24px;
  }

  /* Back */
  .brand {
    position: absolute; right: 40px; top: 50px;
    font-size: 29px; font-weight: 600; color: var(--brand-blue);
    letter-spacing: .2px;
  }
  .services__title {
    position: absolute; left: 24px; top: 111px;
    font-size: 14px; font-weight: 600; color: var(--navy);
  }
  .services { position: absolute; left: 24px; top: 148px; list-style: none; }
  .services li {
    display: flex; align-items: center; height: 25px;
    font-size: 13px; font-weight: 600; color: var(--ink);
  }
  .services svg { width: 18px; height: 16px; margin-right: 11px; fill: var(--navy); }
</style>
</head>
<body>
<main class="stage">

  <section class="card card--front">
    <div class="mascot" role="img" aria-label="Cartoon removalist character in cap and orange shirt giving a thumbs up, leaning on a hand trolley beside a cardboard box"></div>

    <div class="identity">
      <p class="identity__name">Marcus Delane</p>
      <p class="identity__role">Owner Operator</p>
    </div>
    <p class="address">Harbour Vale,QLD 4299</p>

    <ul class="contacts">
      <li>0400 555 182
        <svg viewBox="0 0 10 10"><path d="M2 0.5l1.8 2-1 1.2a6 6 0 0 0 3.5 3.5l1.2-1 2 1.8-1.3 1.5C4.5 9.2 0.8 5.5 0.5 1.8z"/></svg></li>
      <li>07 5550 1234
        <svg viewBox="0 0 10 10"><path d="M2.5 0h5v10h-5zM3.3 1v7h3.4V1z"/><circle cx="5" cy="9" r=".5" fill="#fff"/></svg></li>
      <li>ktwremovals@mailbox.com
        <svg viewBox="0 0 10 10"><path d="M0 2h10v6H0zM0.8 2.6L5 5.6l4.2-3z" fill-rule="evenodd"/></svg></li>
      <li>www.ktwremovals.com.au
        <svg viewBox="0 0 10 10"><path d="M4 6l2-2M3.5 4.5L2 6a1.4 1.4 0 0 0 2 2l1.5-1.5M6.5 5.5L8 4a1.4 1.4 0 0 0-2-2L4.5 3.5" fill="none" stroke="#14246b" stroke-width="1.2" stroke-linecap="round"/></svg></li>
      <li>www.friendnet.com/ktwremovals
        <svg viewBox="0 0 10 10"><circle cx="5" cy="5" r="3.5"/></svg></li>
    </ul>

    <div class="power-band">KTW Removals -The Gentle Movers.</div>
  </section>

  <section class="card card--back">
    <p class="brand">KTW Removals</p>

    <p class="services__title">KTW Removals Provides:</p>
    <ul class="services">
      <li><svg viewBox="0 0 18 16"><path d="M1 3h10v8H1zM11 6h3.5l2.5 3v2h-6z"/><circle cx="4" cy="12.5" r="1.8"/><circle cx="13.5" cy="12.5" r="1.8"/></svg>Local,Country &amp; Interstate Removals</li>
      <li><svg viewBox="0 0 18 16"><path d="M9 1l8 7h-2.5v7h-4v-4.5h-3V15h-4V8H1z"/></svg>Home &amp; Hi Rise Removals</li>
      <li><svg viewBox="0 0 18 16"><path d="M2 1h2l3 10h9v1.8H5.7L3 2.8H2z"/><rect x="8" y="3" width="7" height="6" transform="rotate(-15 11.5 6)"/><circle cx="6.5" cy="14" r="1.6"/></svg>Office &amp; Factory Relocation's</li>
      <li><svg viewBox="0 0 18 16"><path d="M5 1h8l-.5 5a3.5 3.5 0 0 1-7 0zM8.2 9.5h1.6v4H12V15H6v-1.5h2.2z"/></svg>Pre - Packing &amp; Unpacking Service 's</li>
      <li><svg viewBox="0 0 18 16"><rect x="6" y="1" width="7" height="6"/><path d="M1 9h4l3 1.5h4a1 1 0 0 1 0 2H8.5h4.5l4-2.5v2L12 15H1z"/></svg>Storage Solution</li>
    </ul>
  </section>

</main>
</body>
</html>
```